Upgrade my Product Label on my Natural Skincare line

Our current product labels are in need of a slight upgrade. The current labels have worked for the last 11 years, but our main presence is ecommerce, and we need these products to stand out a bit better amongst the competition. Brindlemart is our primary marketplace, and the first image people will see, is our thumbnail.
We have about 10 types of oils, and a line of serums, a line of hair serums, so we need to differentiate these, but also without deviating from the current branding too much. The current customers should still be able to recognize the branding.
The theme should be flexible enough to add a new product, or product line to the brand, and have some marking to make the product differentiate from the other products.
About the brand, we offer natural skincare products, topicals, oils, serums and lotions. Primary demographic is women, 40-65+
The new design will need to feature bigger, and bolder features, like the name, size of the product, so the customer can read this from a thumbnail
Attached are a few different products, and our brand guide. The logo should remain the same, and aspects of the current branding should remain, but open to ideas in any direction.
Target Market(s)
Women 40-65+
Industry/Entity Type
Skincare, Beuty, natural, organic
Font styles to use
Other font styles liked:
- see brand guide for current fonts
Look and feel

```html
<!DOCTYPE html>
<html lang="en">
<head>
<meta charset="utf-8">
<title>Lumera Rose Product Labels</title>
<link rel="stylesheet" href="https://fonts.googleapis.com/css2?family=Great+Vibes&family=Playfair+Display:wght@400;500&family=Montserrat:wght@400;600;700&family=Lora:ital@0;1&display=swap">
<style>
  :root {
    --canvas: #ececec;
    --paper: #ffffff;
    --ink: #3d3438;
    --ink-soft: #6d6266;
    --rose: #e0457f;
    --rose-deep: #c92f6b;
    --pink-light: #f8c6d8;
    --green: #5b7d56;
    --purple: #6a4ea3;
    --yellow: #f2d531;
    --lime: #6db33f;
  }
  * { box-sizing: border-box; margin: 0; padding: 0; }
  html, body { width: 703px; height: 1200px; overflow: hidden; }
  body {
    background: var(--canvas);
    display: flex;
    flex-direction: column;
    align-items: center;
    gap: 40px;
    padding-top: 25px;
    font-family: "Lora", Georgia, serif;
    color: var(--ink);
  }
  .label {
    width: 563px;
    height: 255px;
    display: flex;
    background: var(--paper);
    box-shadow: 0 1px 3px rgba(0,0,0,.12);
  }
  .label--rosemary { --band: var(--green); --badge: var(--lime); --badge-ink: #1f3d12; }
  .label--rose { --band: var(--rose); --badge: var(--yellow); --badge-ink: var(--rose-deep); }
  .label--serum { --band: var(--purple); --badge: var(--yellow); --badge-ink: var(--rose-deep); }

  .usage {
    width: 235px;
    padding: 14px 14px 10px 16px;
    display: flex;
    flex-direction: column;
    position: relative;
  }
  .usage__title {
    font-family: "Montserrat", Arial, sans-serif;
    font-weight: 700;
    font-size: 7.5px;
    letter-spacing: .8px;
    margin-bottom: 2px;
  }
  .usage__heading {
    font-family: "Great Vibes", cursive;
    font-size: 14px;
    line-height: 15px;
    color: var(--ink);
  }
  .usage__text {
    font-size: 6.3px;
    line-height: 8px;
    color: var(--ink-soft);
    margin-bottom: 3px;
  }
  .usage__footer {
    margin-top: auto;
    display: flex;
    gap: 26px;
    font-family: "Montserrat", Arial, sans-serif;
    font-size: 6px;
    color: var(--ink-soft);
  }
  .offer {
    position: absolute;
    right: 12px;
    bottom: 10px;
    width: 36px;
    height: 36px;
    border: 1.5px solid var(--rose);
    border-radius: 50%;
    display: flex;
    align-items: center;
    justify-content: center;
    font-family: "Montserrat", Arial, sans-serif;
    font-weight: 700;
    font-size: 6.5px;
    line-height: 7px;
    text-align: center;
    color: var(--rose);
  }

  .band {
    width: 37px;
    background: var(--band);
    display: flex;
    align-items: center;
    justify-content: center;
  }
  .band__name {
    writing-mode: vertical-rl;
    transform: rotate(180deg);
    font-family: "Playfair Display", Georgia, serif;
    font-size: 17px;
    letter-spacing: 1.5px;
    color: #fff;
    white-space: nowrap;
  }

  .front {
    flex: 1;
    position: relative;
    background:
      radial-gradient(ellipse at 15% 80%, #f6b58f 0%, rgba(246,181,143,0) 35%),
      radial-gradient(ellipse at 85% 20%, #fbdbe6 0%, rgba(251,219,230,0) 40%),
      linear-gradient(125deg, #d8316f 0%, #ef6fa0 35%, #f7b3cb 60%, #e4508a 100%);
    display: flex;
    justify-content: center;
    padding: 16px 0;
  }
  .panel {
    width: 150px;
    background: rgba(255,255,255,.96);
    display: flex;
    flex-direction: column;
    align-items: center;
    text-align: center;
    padding: 14px 8px 10px;
    position: relative;
  }
  .brand {
    display: flex;
    flex-direction: column;
    align-items: center;
    gap: 3px;
    margin-bottom: 14px;
  }
  .brand__dot {
    width: 18px;
    height: 18px;
    border-radius: 50%;
    background: var(--rose);
  }
  .brand__name {
    font-family: "Montserrat", Arial, sans-serif;
    font-weight: 600;
    font-size: 6px;
    letter-spacing: 1.2px;
    color: var(--rose);
  }
  .panel__kicker {
    font-family: "Montserrat", Arial, sans-serif;
    font-size: 6px;
    letter-spacing: 1px;
    color: var(--ink);
    margin-bottom: 4px;
  }
  .panel__product {
    font-family: "Playfair Display", Georgia, serif;
    font-size: 21px;
    line-height: 22px;
    color: var(--rose);
    margin-bottom: 8px;
  }
  .panel__claim {
    font-family: "Montserrat", Arial, sans-serif;
    font-weight: 600;
    font-size: 6px;
    line-height: 8px;
    letter-spacing: .8px;
    color: var(--ink);
  }
  .panel__size {
    margin-top: auto;
    font-family: "Montserrat", Arial, sans-serif;
    font-size: 7px;
    letter-spacing: .5px;
    color: var(--ink-soft);
  }
  .tag {
    position: absolute;
    top: -8px;
    right: -18px;
    width: 44px;
    height: 44px;
    border-radius: 50%;
    background: var(--badge);
    display: flex;
    align-items: center;
    justify-content: center;
    font-family: "Great Vibes", cursive;
    font-size: 13px;
    line-height: 12px;
    color: var(--badge-ink);
    text-align: center;
  }
</style>
</head>
<body>

  <article class="label label--rosemary">
    <section class="usage">
      <h3 class="usage__title">HOW TO USE</h3>
      <h4 class="usage__heading">Key nutrients</h4>
      <p class="usage__text">Massage a small amount of oil into the scalp and hair, leave in overnight after a warm rinse.</p>
      <h4 class="usage__heading">Daily use</h4>
      <p class="usage__text">Apply to dry ends, comb through and style.</p>
      <h4 class="usage__heading">Ingredients</h4>
      <p class="usage__text">Rosmarinus Officinalis Oil, Jojoba Seed Oil, Argan Kernel Oil, Castor Seed Oil, Vitamin E, Lavender Oil, Peppermint Leaf Oil.</p>
      <h4 class="usage__heading">Warnings</h4>
      <p class="usage__text">For external use only. Keep away from eyes and children. Patch test first.</p>
      <div class="usage__footer"><span>60 ml | 2 fl oz</span><span>www.lumerarose.com</span></div>
      <div class="offer">50%<br>OFF</div>
    </section>
    <div class="band"><span class="band__name">ROSEMARY OIL</span></div>
    <section class="front" role="img" aria-label="Soft pink rose petal photograph">
      <div class="panel">
        <div class="tag">Hair<br>Serum</div>
        <div class="brand"><span class="brand__dot"></span><span class="brand__name">LUMERA ROSE</span></div>
        <p class="panel__kicker">100% NATURAL BLEND</p>
        <h2 class="panel__product">Rosemary<br>Hair Oil</h2>
        <p class="panel__claim">PLANT POWERED<br>NOURISHING</p>
        <p class="panel__size">60 ml / 2 fl oz</p>
      </div>
    </section>
  </article>

  <article class="label label--rose">
    <section class="usage">
      <h3 class="usage__title">HOW TO USE</h3>
      <h4 class="usage__heading">Key nutrients</h4>
      <p class="usage__text">Mist over cleansed face and neck, let the water settle into skin before your serum.</p>
      <h4 class="usage__heading">Daily use</h4>
      <p class="usage__text">Spray morning and evening, pat in gently.</p>
      <h4 class="usage__heading">Ingredients</h4>
      <p class="usage__text">Rosa Damascena Flower Water, Aloe Leaf Juice, Glycerin, Colloidal Gold, Rose Hip Extract, Chamomile Water, Vitamin C.</p>
      <h4 class="usage__heading">Warnings</h4>
      <p class="usage__text">For external use only. Keep away from eyes and children. Store cool.</p>
      <div class="usage__footer"><span>60 ml | 2 fl oz</span><span>www.lumerarose.com</span></div>
      <div class="offer">50%<br>OFF</div>
    </section>
    <div class="band"><span class="band__name">ROSE WATER</span></div>
    <section class="front" role="img" aria-label="Soft pink rose petal photograph">
      <div class="panel">
        <div class="tag">Gold<br>Serum</div>
        <div class="brand"><span class="brand__dot"></span><span class="brand__name">LUMERA ROSE</span></div>
        <p class="panel__kicker">REAL 24 CARAT GOLD</p>
        <h2 class="panel__product">Gold Rose<br>Water</h2>
        <p class="panel__claim">100% GLOWING FACE<br>ALL NATURAL</p>
        <p class="panel__size">60 ml / 2 fl oz</p>
      </div>
    </section>
  </article>

  <article class="label label--serum">
    <section class="usage">
      <h3 class="usage__title">HOW TO USE</h3>
      <h4 class="usage__heading">Key nutrients</h4>
      <p class="usage__text">Press three drops into clean skin each morning before moisturiser and sun care.</p>
      <h4 class="usage__heading">Daily use</h4>
      <p class="usage__text">Apply to face and neck, smooth upward.</p>
      <h4 class="usage__heading">Ingredients</h4>
      <p class="usage__text">Argania Spinosa Kernel Oil, Squalane, Rosehip Seed Oil, Niacinamide, Vitamin E, Green Tea Extract, Orange Peel Oil.</p>
      <h4 class="usage__heading">Warnings</h4>
      <p class="usage__text">For external use only. Keep away from eyes and children. Patch test first.</p>
      <div class="usage__footer"><span>60 ml | 2 fl oz</span><span>www.lumerarose.com</span></div>
      <div class="offer">50%<br>OFF</div>
    </section>
    <div class="band"><span class="band__name">MORNING SERUM</span></div>
    <section class="front" role="img" aria-label="Soft pink rose petal photograph">
      <div class="panel">
        <div class="tag">Serum<br>Line</div>
        <div class="brand"><span class="brand__dot"></span><span class="brand__name">LUMERA ROSE</span></div>
        <p class="panel__kicker">60 ml / 2 fl oz</p>
        <h2 class="panel__product">Argan<br>Morning<br>Serum</h2>
        <p class="panel__claim">ALL NATURAL<br>PURE ORGANIC</p>
        <p class="panel__size">60 ml / 2 fl oz</p>
      </div>
    </section>
  </article>

  <article class="label label--rose">
    <section class="usage">
      <h3 class="usage__title">HOW TO USE</h3>
      <h4 class="usage__heading">Key nutrients</h4>
      <p class="usage__text">Smooth a few drops over dry patches, cuticles and fine lines to restore softness.</p>
      <h4 class="usage__heading">Daily use</h4>
      <p class="usage__text">Use nightly on clean skin, massage in.</p>
      <h4 class="usage__heading">Ingredients</h4>
      <p class="usage__text">Tocopherol, Sunflower Seed Oil, Sweet Almond Oil, Rose Hip Oil, Avocado Oil, Carrot Seed Oil, Rosemary Extract.</p>
      <h4 class="usage__heading">Warnings</h4>
      <p class="usage__text">For external use only. Keep away from eyes and children. Store cool.</p>
      <div class="usage__footer"><span>60 ml | 2 fl oz</span><span>www.lumerarose.com</span></div>
      <div class="offer">50%<br>OFF</div>
    </section>
    <div class="band"><span class="band__name">ROSE WATER</span></div>
    <section class="front" role="img" aria-label="Soft pink rose petal photograph">
      <div class="panel">
        <div class="brand"><span class="brand__dot"></span><span class="brand__name">LUMERA ROSE</span></div>
        <p class="panel__kicker">100% PURE ORGANIC</p>
        <h2 class="panel__product">Vitamin E<br>Oil</h2>
        <p class="panel__claim">PLANT BASED FACE<br>ALL NATURAL</p>
        <p class="panel__size">60 ml / 2 fl oz</p>
      </div>
    </section>
  </article>

</body>
</html>
```